Designing a website for Brightmoor Pest Services PTY LTD

Pest control company looking for someone to build an informative website containing services we offer and an online inquiry form.
Commercial premises - Specialising in - Rodent control, stored product pest control, flying insect control, ant, spider and insect control, Termite inspections and treatments. Termite management systems on a commercial scale.
Facilities we service
Commercial - shopping centres, transport facilities, restaurants, pubs, clubs, bars food manufacturing facilities.
Residential - Houses specialising in - Rodent, Ant, Spider, Cockroach and Termite control. Termite inspections, Pre - purchase inspections, Termite treatments, Termite management systems.
Target Market(s)
Mainly commercial and industrial clients and Residential clients.
Industry/Entity Type
Pest Control
Number of Pages Required
1 page
Look and feel

```html
<!DOCTYPE html>
<html lang="en">
<head>
<meta charset="utf-8">
<title>Brightmoor Pest Services</title>
<link href="https://fonts.googleapis.com/css2?family=Poppins:wght@400;500;600;700&display=swap" rel="stylesheet">
<style>
:root{
  --green:#3b8c0c;
  --green-dark:#2f7508;
  --ink:#111;
  --text:#222;
  --muted:#9a9a9a;
  --grey-bg:#f0f0f0;
  --footer:#000;
  --white:#fff;
}
*{margin:0;padding:0;box-sizing:border-box}
html,body{width:1200px;height:2835px;overflow:hidden;background:var(--white)}
body{font-family:'Poppins',sans-serif;color:var(--text);position:relative}
.abs{position:absolute}

/* header */
.site-header{position:absolute;left:0;top:0;width:1200px;height:89px;background:var(--white);z-index:5}
.brand{position:absolute;left:88px;top:22px;width:150px;font-weight:700;font-size:16px;line-height:19px;color:var(--ink);display:flex;align-items:center;gap:8px}
.brand-dot{width:14px;height:14px;border-radius:50%;background:var(--green);flex:none}
.main-nav{position:absolute;left:442px;top:36px;display:flex;gap:33px;font-size:12.5px;font-weight:600;color:var(--ink)}
.main-nav a{color:inherit;text-decoration:none;position:relative}
.main-nav a.active{color:var(--green)}
.main-nav a.active::before{content:"";position:absolute;left:-4px;right:-4px;top:-7px;height:2px;background:var(--green)}
.main-nav a.active::after{content:"";position:absolute;left:-4px;right:-4px;bottom:-7px;height:2px;background:var(--green)}
.btn{display:inline-flex;align-items:center;justify-content:center;border-radius:22px;font-weight:600;text-decoration:none}
.btn-green{background:var(--green);color:var(--white)}
.inquire-btn{position:absolute;left:959px;top:25px;width:152px;height:40px;font-size:15px}

/* hero */
.hero{position:absolute;left:0;top:89px;width:1200px;height:520px}
.hero-photo{position:absolute;inset:0;background:linear-gradient(100deg,#d8d2cc 0%,#c9bfb6 30%,#e8e6e3 55%,#cfc8bf 80%,#b9ab9b 100%)}
.hero-wave{position:absolute;left:0;bottom:0;width:1200px;height:60px}
.hero-sub{position:absolute;left:97px;top:168px;font-size:30px;font-weight:600;color:var(--ink)}
.hero-title{position:absolute;left:96px;top:208px;font-size:44px;font-weight:700;color:var(--ink);letter-spacing:-.5px}
.hero-btn{position:absolute;left:98px;top:282px;width:162px;height:40px;font-size:15px;font-weight:500}

/* about */
.about-photo{position:absolute;left:119px;top:653px;width:376px;height:370px;border-radius:50%;background:linear-gradient(135deg,#c9d2d6 0%,#8fa3ae 50%,#4e6b78 100%)}
.about-title{position:absolute;left:616px;top:693px;font-size:34px;font-weight:700;color:var(--green)}
.about-copy{position:absolute;left:616px;top:762px;width:480px;font-size:14.5px;line-height:17.5px;color:var(--ink)}
.about-copy p{margin-bottom:17px}
.btn-outline{position:absolute;left:616px;top:955px;width:162px;height:40px;border:2px solid var(--ink);color:var(--ink);font-size:14.5px}

/* services */
.services{position:absolute;left:0;top:1095px;width:1200px;height:610px}
.services-bg{position:absolute;inset:0;background:radial-gradient(ellipse at 35% 20%,#b9b9bb 0%,#d7d7d7 40%,#e4ddd3 75%,#d8c8b3 100%)}
.section-title{position:absolute;left:0;width:1200px;text-align:center;font-size:34px;font-weight:700;color:var(--green)}
.service-card{position:absolute;top:1284px;width:439px;height:236px;border:4px solid var(--white);display:flex;align-items:center;justify-content:center;font-size:23px;font-weight:600;color:var(--white);box-shadow:0 2px 6px rgba(0,0,0,.15)}
.card-commercial{left:144px;background:linear-gradient(160deg,#9bb5c9 0%,#3d6478 45%,#1d3442 100%)}
.card-residential{left:615px;background:linear-gradient(180deg,#1f3a55 0%,#2c4a63 45%,#6b5a45 70%,#2d3b2f 100%)}
.service-list{position:absolute;top:1532px;font-size:13.5px;line-height:19.5px;color:var(--ink);text-align:center}
.service-list span{white-space:nowrap;margin:0 4px}
.service-list span::before{content:"➝";font-size:10px;margin-right:5px}

/* testimonials */
.quote-badge{position:absolute;left:570px;top:1801px;width:60px;height:60px;border-radius:50%;background:#ececec}
.testimonial-text{position:absolute;left:210px;top:1880px;width:780px;text-align:center;font-size:14.5px;line-height:20px;color:var(--ink)}
.testimonial-meta{position:absolute;left:0;top:1967px;width:1200px;display:flex;justify-content:center;align-items:center;gap:12px;font-size:12px;color:var(--ink)}
.testimonial-meta .divider{width:1px;height:16px;background:#ccc}
.testimonial-meta strong{font-size:14px;font-weight:600}
.dots{position:absolute;left:576px;top:2015px;display:flex;gap:8px}
.dots i{width:10px;height:10px;border-radius:50%;border:1px solid #999}
.dots i.on{background:var(--green);border-color:var(--green)}

/* inquiry */
.inquiry{position:absolute;left:0;top:2055px;width:1200px;height:460px}
.field{position:absolute;height:30px;border-bottom:1px solid #9a9a9a;font-size:14px;color:#555;display:flex;align-items:center;gap:10px;padding-left:10px}
.field svg{flex:none}
.submit-btn{position:absolute;left:533px;top:2394px;width:134px;height:40px;font-size:16px;border-radius:22px}

/* footer */
.site-footer{position:absolute;left:0;top:2514px;width:1200px;height:282px;background:var(--footer);color:#bbb}
.footer-brand{position:absolute;left:90px;top:95px;width:170px;font-size:21px;font-weight:700;line-height:25px;color:var(--white)}
.socials{position:absolute;left:92px;top:204px;display:flex;gap:22px}
.socials i{width:17px;height:17px;border-radius:50%;border:2px solid var(--white)}
.footer-heading{position:absolute;top:61px;font-size:18px;font-weight:600;color:var(--green)}
.quick-links{position:absolute;left:328px;top:98px;list-style:none;font-size:13px;line-height:26.5px}
.quick-links li:first-child{color:var(--green);text-decoration:underline}
.contact-item{position:absolute;left:513px;display:flex;gap:14px;font-size:13.5px;line-height:19px;color:#ccc}
.map{position:absolute;left:800px;top:56px;width:312px;height:176px;border-radius:6px;background:linear-gradient(135deg,#eef1f4 0%,#e3e7ea 60%,#dfe6ec 100%)}
.copyright{position:absolute;left:0;top:2796px;width:1200px;height:39px;background:var(--green);color:var(--white);font-size:14px;display:flex;align-items:center;justify-content:center}
</style>
</head>
<body>

<header class="site-header">
  <div class="brand"><span class="brand-dot"></span>Brightmoor Pest Services</div>
  <nav class="main-nav">
    <a class="active" href="#">HOME</a>
    <a href="#">ABOUT US</a>
    <a href="#">SERVICES</a>
    <a href="#">TESTIMONIALS</a>
    <a href="#">CONTACT US</a>
  </nav>
  <a class="btn btn-green inquire-btn" href="#">Inquire Now</a>
</header>

<section class="hero">
  <div class="hero-photo" role="img" aria-label="Pest control technician in protective suit spraying treatment inside a home"></div>
  <svg class="hero-wave" viewBox="0 0 1200 60" preserveAspectRatio="none"><path d="M0 60 C250 10 450 0 620 0 C850 0 1050 25 1200 60 Z" fill="#fff"/></svg>
  <div class="hero-sub">We are the Experts</div>
  <h1 class="hero-title">IN PEST CONTROL</h1>
  <a class="btn btn-green hero-btn" href="#">Explore More</a>
</section>

<section class="about">
  <div class="about-photo" role="img" aria-label="Technician in respirator mask treating a commercial kitchen"></div>
  <h2 class="about-title">About Us</h2>
  <div class="about-copy">
    <p>Lorem Ipsum is simply dummy text of the printing and typesetting industry.</p>
    <p>Lorem Ipsum has been the industry's standard dummy text ever since the 1500s, when an unknown printer took a galley of type and scrambled it to make a type specimen book.</p>
    <p>It has survived not only five centuries, but also the leap into electronic typesetting, remaining essentially unchanged.</p>
  </div>
  <a class="btn btn-outline" href="#">Explore More</a>
</section>

<section class="services">
  <div class="services-bg" role="img" aria-label="Blurred technician spraying indoors"></div>
  <svg class="abs" style="left:0;top:0" width="1200" height="610" viewBox="0 0 1200 610" preserveAspectRatio="none">
    <path d="M0 0 L0 4 C300 50 700 45 1200 0 Z" fill="#fff"/>
    <path d="M0 610 L1200 610 L1200 605 C900 560 500 550 0 600 Z" fill="#fff"/>
  </svg>
</section>
<h2 class="section-title" style="top:1200px">Services</h2>
<div class="service-card card-commercial" role="img" aria-label="Glass office towers">COMMERCIAL</div>
<div class="service-card card-residential" role="img" aria-label="Modern house at dusk">RESIDENTIAL</div>
<div class="service-list" style="left:144px;width:439px">
  <span>Shopping Centres</span><span>Transport Facilities</span><span>Restaurants</span><br>
  <span>Pubs</span><span>Clubs</span><span>Bars Food Manufacturing Facilities</span>
</div>
<div class="service-list" style="left:615px;width:439px">
  <span>Rodent</span><span>Ant</span><span>Spider</span><span>Cockroach and Termite control</span><br>
  <span>Termite inspections</span><span>Pre - purchase inspections</span><span>Termite</span><br>
  treatments <span>Termite management systems</span>
</div>

<h2 class="section-title" style="top:1733px">Testimonials</h2>
<div class="quote-badge">
  <svg width="60" height="60" viewBox="0 0 60 60"><path d="M17 40 L17 31 C17 24 20 20 27 19 L27 24 C23 25 22 27 22 30 L27 30 L27 40 Z M32 40 L32 31 C32 24 35 20 42 19 L42 24 C38 25 37 27 37 30 L42 30 L42 40 Z" fill="#3b8c0c"/></svg>
</div>
<p class="testimonial-text">Lorem Ipsum is simply dummy text of the printing and typesetting industry. Lorem Ipsum has been the industry's standard dummy text ever since the 1500s, when an unknown printer took a galley of type and scrambled it to make a type specimen book.</p>
<div class="testimonial-meta">
  <svg width="15" height="15" viewBox="0 0 15 15"><rect x="1" y="2.5" width="13" height="11" rx="1" fill="none" stroke="#3b8c0c" stroke-width="1.6"/><path d="M1 6h13M4.5 1v3M10.5 1v3" stroke="#3b8c0c" stroke-width="1.6"/></svg>
  <span>30 Nov, 2020</span><span class="divider"></span><strong>Dana Whitfield</strong>
</div>
<div class="dots"><i></i><i class="on"></i><i></i></div>

<section class="inquiry">
  <svg class="abs" style="left:0;top:0" width="1200" height="460" viewBox="0 0 1200 460" preserveAspectRatio="none">
    <path d="M0 0 C400 55 800 55 1200 0 L1200 460 L0 460 Z" fill="#f0f0f0"/>
  </svg>
</section>
<h2 class="section-title" style="top:2170px">Quick Inquiry</h2>
<div class="field" style="left:201px;top:2250px;width:250px">
  <svg width="13" height="14" viewBox="0 0 13 14"><circle cx="6.5" cy="4" r="3" fill="none" stroke="#3b8c0c" stroke-width="1.5"/><path d="M1 13c0-3 2.5-5 5.5-5s5.5 2 5.5 5" fill="none" stroke="#3b8c0c" stroke-width="1.5"/></svg>Name</div>
<div class="field" style="left:475px;top:2250px;width:250px">
  <svg width="10" height="14" viewBox="0 0 10 14"><rect x="1" y="1" width="8" height="12" rx="1.5" fill="none" stroke="#3b8c0c" stroke-width="1.5"/><path d="M4 11h2" stroke="#3b8c0c" stroke-width="1.5"/></svg>Phone</div>
<div class="field" style="left:749px;top:2250px;width:250px">
  <svg width="15" height="11" viewBox="0 0 15 11"><rect x="1" y="1" width="13" height="9" fill="none" stroke="#3b8c0c" stroke-width="1.5"/><path d="M1 1l6.5 5L14 1" fill="none" stroke="#3b8c0c" stroke-width="1.5"/></svg>Email</div>
<div class="field" style="left:201px;top:2322px;width:798px">
  <svg width="14" height="14" viewBox="0 0 14 14"><path d="M1 1h12v8l-4 4H1Z" fill="none" stroke="#3b8c0c" stroke-width="1.5"/></svg>Message</div>
<a class="btn btn-green submit-btn" href="#">Submit</a>

<footer class="site-footer">
  <div class="footer-brand">Brightmoor Pest Services</div>
  <div class="socials"><i></i><i></i><i></i><i></i></div>
  <div class="footer-heading" style="left:328px">Quick Link</div>
  <ul class="quick-links">
    <li>Home</li><li>About Us</li><li>Services</li><li>Testimonials</li><li>Contact Us</li>
  </ul>
  <div class="footer-heading" style="left:513px">Conatct info</div>
  <div class="contact-item" style="top:99px">
    <svg width="14" height="18" viewBox="0 0 14 18"><path d="M7 17C3 11 1 8.5 1 6a6 6 0 0 1 12 0c0 2.5-2 5-6 11Z" fill="none" stroke="#3b8c0c" stroke-width="2"/><circle cx="7" cy="6" r="2" fill="#3b8c0c"/></svg>
    <span>lorem ipsum, 88 Harbour Lane<br>Eastfield, NL &nbsp; B2K 4T7</span></div>
  <div class="contact-item" style="top:158px">
    <svg width="14" height="14" viewBox="0 0 14 14"><path d="M3 1l2.5 3-1.5 2c1 2 2 3 4 4l2-1.5 3 2.5-1.5 2.5C7 13 1 7 .5 2.5Z" fill="#3b8c0c"/></svg>
    <span>555.214.0398</span></div>
  <div class="contact-item" style="top:196px">
    <svg width="16" height="12" viewBox="0 0 16 12"><rect x="0" y="0" width="16" height="12" fill="#3b8c0c"/><path d="M0 0l8 6 8-6" fill="none" stroke="#000" stroke-width="1.3"/></svg>
    <span>hello@brightmoorpest.com</span></div>
  <div class="map" role="img" aria-label="Street map showing the office location"></div>
</footer>
<div class="copyright">Copyright © 2021 Brightmoor Pest Services. All Rights Reserved</div>

</body>
</html>
```